Vantor Reach Unique Marketing Website Design

I am starting a new company that is a thought leader in the marketing consulting space. The company is called Vantor Reach. We intend to build a Wordpress site on the Astra Theme with the Spectra builder. Our goal is to become the leading voice that empowers high-ticket service business leaders to become Vantor Reach by equipping them with the cutting-edge frameworks and decision grade intelligence taught in leading business schools. What we are looking for is a website design that is clean and professional, making some use of white space well also being eye catching and distinctive in the consulting space. We will probably want to have a video on the homepage not in the hero section, but just below to explain the company and what we do. Our tagline is "Be found. Be chosen." I have attached a brand guide with some messaging, our typography choices, and our color system. The full site will have a primary nav that is four pages - About us, Services, Insights (essentially a blog), and Contact Us. The goal of this project is to develop an art direction that I can give to a designer to build loads of new pages.

Target Market(s)

Business owners (mostly male) from 30-60 years old, looking to fix their sales and marketing funnel.

Industry/Entity Type

Marketing consulting

Font styles to use
Sans Serif

Requirements
Must have
• A clean, professional design that builds trust with owners of high-ticket service businesses. We need a space for explainer video, and sections that tell prospects what we do. Would also like to have a blog carousel.
Nice to have
• Social feeds, if possible. See attached documents for colors and fonts.
Should not have
• Our feel is professional enough to be trustworthy, but unique enough to be memorable. Cartoon ideas do not meet the professional test, and we do not want the website to appear feminine.

```html
<!DOCTYPE html>
<html lang="en">
<head>
<meta charset="utf-8">
<title>Vantor Reach — Be Found. Be Chosen.</title>
<link href="https://fonts.googleapis.com/css2?family=Oswald:wght@500;600&family=Poppins:wght@400;500;600&display=swap" rel="stylesheet">
<style>
:root{
  --blue:#0b6fdf;
  --blue-dark:#1f4fa8;
  --green:#18a957;
  --ink:#2a2a2a;
  --text:#555;
  --muted:#8a8a8a;
  --band:#f4f3f3;
  --footer:#2d2d2d;
  --white:#fff;
}
*{box-sizing:border-box;margin:0;padding:0}
html,body{width:1200px;height:3633px;overflow:hidden}
body{position:relative;background:var(--white);font-family:"Poppins",sans-serif;color:var(--text)}
.abs{position:absolute}
.display{font-family:"Oswald",sans-serif;font-weight:600;color:var(--ink)}
.eyebrow{font-family:"Oswald",sans-serif;font-weight:500;font-size:10px;line-height:14px;letter-spacing:.3px;color:var(--green);text-transform:uppercase}
.btn{position:absolute;background:var(--blue);color:var(--white);font-size:11px;font-weight:500;display:flex;align-items:center;justify-content:center;border-radius:2px}
.center{left:0;width:1200px;text-align:center}

/* hero */
.hero{position:absolute;left:0;top:0;width:1200px;height:523px;overflow:hidden;background:linear-gradient(100deg,#1b1d20 0%,#2c3036 35%,#4a4e55 60%,#6d747d 80%,#4d5560 100%)}
.hero-shade{position:absolute;inset:0;background:linear-gradient(90deg,rgba(10,12,15,.75) 0%,rgba(10,12,15,.35) 55%,rgba(10,12,15,.1) 100%)}
.brand{position:absolute;display:flex;align-items:center;gap:8px;font-family:"Poppins",sans-serif;font-weight:600;font-size:19px;color:var(--white);letter-spacing:.5px}
.brand i{display:block;width:12px;height:12px;background:var(--blue)}
.nav{position:absolute;left:471px;top:40px;font-size:10.5px;color:var(--white)}
.nav a{color:var(--white);text-decoration:none;position:absolute;white-space:nowrap}
.hero h1{position:absolute;left:234px;top:176px;font-family:"Oswald",sans-serif;font-weight:600;color:var(--white);font-size:62px;line-height:75px}
.hero p{position:absolute;left:234px;top:327px;width:390px;font-size:12.5px;line-height:15px;color:#eee}
.arrow{position:absolute;width:36px;height:36px;border-radius:50%;display:flex;align-items:center;justify-content:center}

/* about */
.about-media{left:234px;top:585px;width:337px;height:381px;border-radius:4px;background:linear-gradient(135deg,#c9d3dc 0%,#8796a6 45%,#3e4a57 100%)}
.about-copy{left:629px;top:630px;width:342px}
.about-copy h2{font-size:26px;line-height:30px;margin-top:10px}
.about-copy .lead{margin-top:24px}
.about-copy p{font-size:9.2px;line-height:15.5px;margin-top:4px;color:#555}

/* process */
.step{position:absolute;width:240px;text-align:center}
.step h3{font-family:"Oswald",sans-serif;font-weight:500;font-size:15px;color:var(--ink)}
.step p{font-size:11px;line-height:16px;margin-top:6px;color:#555}

/* services */
.band{left:0;top:1327px;width:1200px;height:715px;background:var(--band)}
.svc-img{position:absolute;width:349px;height:182px;border-radius:2px}
.svc-title{position:absolute;font-family:"Oswald",sans-serif;font-weight:500;font-size:15.5px;color:var(--ink)}

/* team */
.member-photo{position:absolute;top:2183px;width:168px;height:222px}
.member-card{position:absolute;top:2383px;width:132px;height:58px;background:var(--white);box-shadow:0 3px 10px rgba(0,0,0,.1);text-align:center;padding-top:14px}
.member-card b{display:block;font-size:11px;font-weight:600;color:var(--ink)}
.member-card span{display:block;font-size:8px;color:var(--muted);margin-top:2px}

/* articles */
.post{position:absolute;width:229px;height:343px;border:1px solid #ececec;background:var(--white);overflow:hidden}
.post-img{position:absolute;left:0;top:0;width:229px;height:171px}
.post-body{position:absolute;left:16px;right:14px;top:188px}
.post-date{font-size:9.5px;color:#444}
.post-title{font-size:14px;line-height:20px;color:var(--ink);margin-top:6px;letter-spacing:-.4px}
.post-excerpt{font-size:7.5px;line-height:13px;color:var(--muted);margin-top:9px}
.read{position:absolute;left:16px;bottom:14px;font-size:7px;font-weight:600;color:var(--ink);display:flex;align-items:center;gap:4px}
.read i{width:11px;height:11px;border:1px solid currentColor;border-radius:50%;display:block}
.post.overlay .post-img{height:343px}
.post.overlay .shade{position:absolute;inset:0;background:linear-gradient(180deg,rgba(0,0,0,0) 50%,rgba(0,0,0,.65) 100%)}
.post.overlay .post-body{top:auto;bottom:42px}
.post.overlay .post-date,.post.overlay .post-title,.post.overlay .read{color:var(--white)}

/* footer */
.footer{left:0;top:3401px;width:1200px;height:232px;background:var(--footer)}
.footer p{font-size:10px;line-height:13px;color:#ddd}
.flink{position:absolute;font-size:10.5px;color:#eee}
.flabel{position:absolute;font-size:8.5px;color:#bbb}
.fbig{position:absolute;font-size:16px;color:var(--white);font-weight:500}
</style>
</head>
<body>

<!-- hero -->
<section class="hero">
  <div class="abs" role="img" aria-label="Smiling businessman shaking hands with a colleague in a bright office" style="inset:0;background:radial-gradient(ellipse at 72% 35%,#8f8a84 0%,#5a5d63 30%,rgba(40,44,50,0) 70%)"></div>
  <div class="hero-shade"></div>
  <svg class="abs" style="left:0;top:0" width="1200" height="523" aria-hidden="true">
    <defs><linearGradient id="beam" x1="0" y1="0" x2="1" y2="1">
      <stop offset="0" stop-color="#1a73e8" stop-opacity=".95"/><stop offset="1" stop-color="#1a4fb0" stop-opacity=".75"/></linearGradient></defs>
    <polygon points="915,0 1000,0 790,523 720,523" fill="url(#beam)"/>
    <polygon points="1000,0 1060,0 860,523 790,523" fill="#2a66c9" opacity=".25"/>
  </svg>
  <div class="brand" style="left:234px;top:36px"><i></i>VANTOR REACH</div>
  <nav class="nav">
    <a style="left:0">Home</a><a style="left:67px">About Us</a><a style="left:149px">Services</a><a style="left:225px">Blog</a><a style="left:285px">Contact Us</a>
  </nav>
  <div class="btn" style="left:853px;top:32px;width:112px;height:31px;font-size:10.5px">Appointment&nbsp;&nbsp;›</div>
  <h1>Be Found.<br>Be Chosen</h1>
  <p>Imagine a future where the work we do together makes a difference in people's lives. The future is here.</p>
  <div class="btn" style="left:234px;top:374px;width:100px;height:29px">Learn More</div>
  <div class="arrow" style="left:51px;top:247px">
    <svg width="14" height="14"><path d="M9 2 L4 7 L9 12" stroke="#fff" stroke-width="1.5" fill="none"/></svg></div>
  <div class="arrow" style="left:1113px;top:247px;background:rgba(60,60,60,.8)">
    <svg width="14" height="14"><path d="M5 2 L10 7 L5 12" stroke="#fff" stroke-width="1.5" fill="none"/></svg></div>
</section>

<!-- about -->
<div class="abs about-media" role="img" aria-label="Explainer video poster: two consultants reviewing a clipboard in an office"></div>
<svg class="abs" style="left:362px;top:723px" width="82" height="82" aria-hidden="true">
  <circle cx="41" cy="41" r="40" fill="#fff" opacity=".35"/><polygon points="33,28 33,54 56,41" fill="#2f63e0"/>
</svg>
<div class="abs about-copy">
  <div class="eyebrow">About Company</div>
  <h2 class="display">Creating A Business With<br>Vantor Reach</h2>
  <p class="lead">Our power of choices is untrammelled and when nothing prevents to do what we like best principle of selection.</p>
  <p>Every pleasures is to welcomed pain avoided owing to the duty the obligations of business it will frequently occur that pleasures have be repudiated and annoyances accepted.</p>
  <p>Every pleasures is to welcomed pain avoided owing to the duty the obligations of business it will frequently occur that pleasures have be repudiated and annoyances accepted.</p>
</div>
<div class="btn" style="left:629px;top:886px;width:100px;height:29px">Learn More</div>

<!-- process -->
<div class="abs center eyebrow" style="top:1025px">Work Process</div>
<h2 class="abs center display" style="top:1036px;font-size:26px">How We Help You Succeed</h2>

<svg class="abs" style="left:268px;top:1105px" width="88" height="88" aria-hidden="true">
  <circle cx="44" cy="44" r="43" fill="none" stroke="var(--blue)" stroke-width="1.3" stroke-dasharray="4 3"/>
  <circle cx="44" cy="44" r="21" fill="none" stroke="var(--blue)" stroke-width="3"/>
  <circle cx="44" cy="44" r="13" fill="none" stroke="var(--blue)" stroke-width="3"/>
  <circle cx="44" cy="44" r="5" fill="var(--blue)"/>
  <path d="M44 44 L60 28" stroke="var(--blue)" stroke-width="2.5"/><path d="M57 24 L64 24 L64 31" stroke="var(--blue)" stroke-width="2.5" fill="none"/>
</svg>
<svg class="abs" style="left:554px;top:1105px" width="88" height="88" aria-hidden="true">
  <circle cx="44" cy="44" r="43" fill="none" stroke="var(--blue)" stroke-width="1.3" stroke-dasharray="4 3"/>
  <rect x="25" y="48" width="6" height="12" fill="var(--blue)"/><rect x="34" y="42" width="6" height="18" fill="var(--blue)"/>
  <rect x="43" y="36" width="6" height="24" fill="var(--blue)"/>
  <path d="M30 63 Q56 62 58 30" stroke="var(--blue)" stroke-width="5" fill="none"/><polygon points="51,32 58,20 65,32" fill="var(--blue)"/>
</svg>
<svg class="abs" style="left:839px;top:1105px" width="88" height="88" aria-hidden="true">
  <circle cx="44" cy="44" r="43" fill="none" stroke="var(--blue)" stroke-width="1.3" stroke-dasharray="4 3"/>
  <rect x="24" y="50" width="7" height="12" fill="var(--blue)"/><rect x="34" y="44" width="7" height="18" fill="var(--blue)"/>
  <rect x="44" y="40" width="7" height="22" fill="var(--blue)"/><rect x="54" y="34" width="7" height="28" fill="var(--blue)"/>
  <path d="M24 44 L40 34 L48 38 L62 26" stroke="var(--blue)" stroke-width="2.5" fill="none"/><polygon points="57,23 66,22 64,31" fill="var(--blue)"/>
  <rect x="20" y="63" width="46" height="2" fill="var(--blue)"/>
</svg>

<div class="step" style="left:192px;top:1208px"><h3>Strategic Frameworks</h3><p>Lorem Ipsum is simply dummy text of the printing and typesetting industry.</p></div>
<div class="step" style="left:478px;top:1208px"><h3>Data-Driven Insights</h3><p>Lorem Ipsum is simply dummy text of the printing and typesetting industry.</p></div>
<div class="step" style="left:766px;top:1208px"><h3>Growth Acceleration</h3><p>Lorem Ipsum is simply dummy text of the printing and typesetting industry.</p></div>

<!-- services -->
<section class="abs band"></section>
<div class="abs center eyebrow" style="top:1362px">What We Do</div>
<h2 class="abs center display" style="top:1374px;font-size:26px">Our Services</h2>

<div class="svc-img" style="left:234px;top:1450px;background:linear-gradient(120deg,#e8ecf0 0%,#8a96a4 40%,#2c3440 100%)" role="img" aria-label="Team presenting revenue charts on a whiteboard"></div>
<div class="svc-img" style="left:616px;top:1450px;background:linear-gradient(120deg,#dfe6ec 0%,#a4b0bc 40%,#2f3945 100%)" role="img" aria-label="Two executives reviewing documents together"></div>
<div class="svc-title" style="left:234px;top:1647px">Revenue Intelligence</div>
<div class="svc-title" style="left:616px;top:1647px">Revenue Psychology</div>

<div class="svc-img" style="left:234px;top:1708px;background:linear-gradient(120deg,#d9d4cc 0%,#9a8f82 45%,#4a4640 100%)" role="img" aria-label="Meeting room table with laptops and people collaborating"></div>
<div class="svc-img" style="left:616px;top:1708px;background:linear-gradient(120deg,#dde7f0 0%,#9fb0c2 45%,#3a4656 100%)" role="img" aria-label="Business team gathered around a table in discussion"></div>
<div class="svc-title" style="left:234px;top:1906px">Demand Architecture</div>
<div class="svc-title" style="left:616px;top:1906px">Advisory / Office Hours</div>

<div class="btn" style="left:550px;top:1974px;width:99px;height:30px">View All</div>

<!-- team -->
<div class="abs center eyebrow" style="top:2089px">Our Team</div>
<h2 class="abs center display" style="top:2101px;font-size:26px">Professional Team Members</h2>

<div class="member-photo" style="left:234px;background:linear-gradient(160deg,#6f7f7a 0%,#3b4448 60%,#1e2428 100%)" role="img" aria-label="Portrait of team member in a dark suit"></div>
<div class="member-photo" style="left:422px;background:linear-gradient(160deg,#3d4fb8 0%,#2a2f6a 60%,#1a1c2e 100%)" role="img" aria-label="Portrait of team member against a blue backdrop"></div>
<div class="member-photo" style="left:609px;background:linear-gradient(160deg,#b8b8ba 0%,#8a8c90 60%,#4a4e58 100%)" role="img" aria-label="Portrait of team member in a blue blazer"></div>
<div class="member-photo" style="left:797px;background:linear-gradient(160deg,#cfd4d8 0%,#7c848c 55%,#2a2e33 100%)" role="img" aria-label="Portrait of team member in a black suit"></div>

<div class="member-card" style="left:252px"><b>Carla Brennan</b><span>Founder &amp; CEO</span></div>
<div class="member-card" style="left:440px"><b>Martin Keller</b><span>Regional Leader</span></div>
<div class="member-card" style="left:627px"><b>Ravi Sandoval</b><span>Managing Partner</span></div>
<div class="member-card" style="left:815px"><b>Owen Hartley</b><span>Chief Executive</span></div>

<!-- articles -->
<div class="abs center eyebrow" style="top:2490px">Latest Articles</div>
<h2 class="abs center display" style="top:2502px;font-size:26px">Latest Articles</h2>

<article class="post" style="left:235px;top:2573px">
  <div class="post-img" role="img" aria-label="Open office with sticky notes on a wall" style="background:linear-gradient(135deg,#f1efe9 0%,#d6cfc3 55%,#9c8e7c 100%)"></div>
  <div class="post-body"><div class="post-date">March 11, 2026</div>
    <div class="post-title">Why Purpose-Driven Employers Succeed</div>
    <div class="post-excerpt">Taking seamless key performance indicators offline to maximise the long tail. Keeping your eye on the ball while performing a deep dive...</div></div>
  <div class="read">READ MORE <i></i></div>
</article>
<article class="post overlay" style="left:485px;top:2573px">
  <div class="post-img" role="img" aria-label="Businessman walking on a city street" style="background:linear-gradient(180deg,#8a8e92 0%,#5c5650 50%,#3a3530 100%)"></div><div class="shade"></div>
  <div class="post-body"><div class="post-date">January 10, 2022</div>
    <div class="post-title">What Does The Future Of Recruitment Look Like?</div></div>
  <div class="read">READ MORE <i></i></div>
</article>
<article class="post" style="left:735px;top:2573px">
  <div class="post-img" role="img" aria-label="Smiling professional woman portrait" style="background:linear-gradient(135deg,#3b4a5c 0%,#7d8a98 50%,#c7b9a8 100%)"></div>
  <div class="post-body"><div class="post-date">March 11, 2026</div>
    <div class="post-title">Statistics You Need to Share With Your Leaders</div>
    <div class="post-excerpt">Holistically pontificate installed base portals after maintainable products. Proactively engage worldwide methodologies with technology...</div></div>
  <div class="read">READ MORE <i></i></div>
</article>

<article class="post overlay" style="left:235px;top:2937px">
  <div class="post-img" role="img" aria-label="Two colleagues talking in a bright lounge" style="background:linear-gradient(180deg,#b9a493 0%,#8f9a8c 50%,#4d5a52 100%)"></div><div class="shade"></div>
  <div class="post-body"><div class="post-date">January 9, 2022</div>
    <div class="post-title">The 4 Most Effective Incentives for Employees</div></div>
  <div class="read">READ MORE <i></i></div>
</article>
<article class="post" style="left:485px;top:2937px">
  <div class="post-img" role="img" aria-label="Woman reading beside a bookshelf" style="background:linear-gradient(135deg,#6b4e34 0%,#a88858 50%,#d8c27a 100%)"></div>
  <div class="post-body"><div class="post-date">March 11, 2026</div>
    <div class="post-title">How Employer Teams Can Respond to a Crisis</div>
    <div class="post-excerpt">Energistically scale future-proof core competencies vis-a-vis impactful experiences. Dramatically synthesize integrated schemas wit...</div></div>
  <div class="read">READ MORE <i></i></div>
</article>
<article class="post overlay" style="left:735px;top:2937px">
  <div class="post-img" role="img" aria-label="Person working on a laptop on a sofa" style="background:linear-gradient(180deg,#a79a80 0%,#7a6e5a 50%,#3e372c 100%)"></div><div class="shade"></div>
  <div class="post-body"><div class="post-date">January 9, 2022</div>
    <div class="post-title">Coping Under the Current Economic Climate</div></div>
  <div class="read">READ MORE <i></i></div>
</article>

<div class="btn" style="left:550px;top:3321px;width:99px;height:30px">View All Blog</div>

<!-- footer -->
<footer class="abs footer">
  <div class="brand" style="left:234px;top:59px"><i></i>VANTOR REACH</div>
  <p class="abs" style="left:234px;top:103px;width:282px">Best a to first of to chooses that was pattern. From to have highly epic either she hopes forth. Ourselves, effects That in thin because derived just then the they queen, one people away, then into the my the or big and in break.</p>
  <div class="flink" style="left:580px;top:53px">Home</div><div class="flink" style="left:648px;top:53px">Team</div>
  <div class="flink" style="left:580px;top:90px">About Us</div><div class="flink" style="left:648px;top:90px">Blog</div>
  <div class="flink" style="left:580px;top:127px">Services</div><div class="flink" style="left:648px;top:127px">Contacts</div>
  <div class="flabel" style="left:745px;top:53px">Have Any Question?</div>
  <div class="fbig" style="left:745px;top:66px">+10 555 20417</div>
  <div class="flabel" style="left:745px;top:98px">Our Mailbox</div>
  <div class="fbig" style="left:745px;top:111px">hello@vantorreach.example</div>
  <div class="flabel" style="left:745px;top:167px">Social Links</div>
  <svg class="abs" style="left:745px;top:183px" width="40" height="12" aria-hidden="true">
    <circle cx="5" cy="6" r="4" fill="#fff"/><rect x="30" y="2" width="8" height="8" fill="#fff"/>
  </svg>
</footer>

</body>
</html>
```